Emerging Australian photographer

I'm based in Cunderdin, a small rural town in the Wheatbelt area of Western Australia. So its a good thing that I love to travel further afield both for pleasure and for work. To me that is one and the same thing in any event!

My desire is to take photos that make the viewers heart skip. I love taking photos of people doing the things they love or being with the people they love. For me, the joy of photography comes with capturing the 'moments between the moments'. I like candid photography best of all - like when the new husband is staring joyfully at his bride and at that minute is unaware of the photographer capturing the moment.

I am available for weddings, engagements, birthdays, special events, newborns, family or individual portraits. By the end of the year I will be accredited with the Coastal Guild of Image Artisans.

I need a card that stands out but is elegant and would sit well on the table at a wedding or be given out in the church grounds. Classy and a little bit sassy.

Target Market(s)

Consumers who are seeking photographic services, eg wedding guests who see me at work and make enquiries.

Industry/Entity Type

Church

Contact Information for Business Card

Tamsin Bexley Photography
Tamsin Bexley
0452 307 618
www.tamsinbexley.com.au
photos@tamsinbexley.com.au

Requirements
Must have
• Must fit with the theme in the watermarks, but be crisp and modern.
Nice to have
• However it's not essential to have the pink! Facebook and Twitter logos.
Should not have
• Old style fonts like times new roman.

```html
<!DOCTYPE html>
<html lang="en">
<head>
<meta charset="utf-8">
<title>Tamsin Bexley Photography – Business Card</title>
<link rel="stylesheet" href="https://fonts.googleapis.com/css2?family=Mulish:wght@300;400;600&display=swap">
<style>
  :root {
    --paper: #ffffff;
    --ink-grey: #6b6b6b;
    --ink-soft: #8a8a8a;
    --rose: #ef86b5;
    --rose-light: #f6b8d2;
    --edge: #e6e6e6;
  }
  html, body {
    margin: 0;
    padding: 0;
    overflow: hidden;
    background: var(--paper);
  }
  .canvas {
    position: relative;
    width: 1200px;
    height: 2250px;
    background: var(--paper);
    font-family: "Mulish", "Helvetica Neue", Arial, sans-serif;
    overflow: hidden;
  }

  /* Card back */
  .card-back {
    position: absolute;
    left: 21px;
    top: 12px;
    width: 1140px;
    height: 713px;
  }
  .card-back__band {
    position: absolute;
    left: 0;
    top: 0;
    width: 68px;
    height: 100%;
    background: var(--rose);
  }
  .card-back__brand {
    position: absolute;
    left: 111px;
    top: 205px;
  }
  .card-back__contact {
    position: absolute;
    left: 0;
    width: 1044px;
    top: 468px;
    margin: 0;
    text-align: right;
    font-style: normal;
    color: var(--ink-soft);
    font-weight: 300;
    font-size: 30px;
    line-height: 47px;
    letter-spacing: 0.3px;
  }
  .contact__name {
    color: var(--ink-grey);
    font-weight: 600;
    font-size: 32px;
  }
  .contact__phone {
    color: var(--rose);
    font-weight: 600;
    font-size: 32px;
    margin-left: 14px;
  }

  /* Wordmark */
  .wordmark {
    display: flex;
    align-items: center;
    gap: 14px;
    color: var(--ink-grey);
    font-weight: 400;
    white-space: nowrap;
  }
  .wordmark__dot {
    flex: none;
    border-radius: 50%;
    background: var(--rose-light);
  }
  .wordmark--small { font-size: 30px; }
  .wordmark--small .wordmark__dot { width: 16px; height: 16px; }
  .wordmark--large { font-size: 50px; }
  .wordmark--large .wordmark__dot { width: 26px; height: 26px; }

  .logo-showcase {
    position: absolute;
    left: 0;
    top: 1035px;
    width: 1200px;
    display: flex;
    justify-content: center;
  }

  /* Card front */
  .card-front {
    position: absolute;
    left: 220px;
    top: 1560px;
    width: 760px;
    height: 465px;
    border: 1px solid var(--edge);
    background: var(--paper);
    display: flex;
    align-items: center;
    justify-content: center;
  }
  .card-front .wordmark { font-size: 38px; }
  .card-front .wordmark__dot { width: 20px; height: 20px; }
</style>
</head>
<body>
<main class="canvas">

  <section class="card-back" aria-label="Business card back">
    <div class="card-back__band"></div>
    <div class="card-back__brand wordmark wordmark--small">
      <span class="wordmark__dot"></span>
      <span class="wordmark__name">tamsin bexley photography</span>
    </div>
    <address class="card-back__contact">
      <div><span class="contact__name">Tamsin Bexley</span><span class="contact__phone">0452 307 618</span></div>
      <div class="contact__web">www.tamsinbexley.com.au</div>
      <div class="contact__email">photos@tamsinbexley.com.au</div>
    </address>
  </section>

  <section class="logo-showcase" aria-label="Brand name">
    <div class="wordmark wordmark--large">
      <span class="wordmark__dot"></span>
      <span class="wordmark__name">tamsin bexley photography</span>
    </div>
  </section>

  <section class="card-front" aria-label="Business card front">
    <div class="wordmark">
      <span class="wordmark__dot"></span>
      <span class="wordmark__name">tamsin bexley photography</span>
    </div>
  </section>

</main>
</body>
</html>
```